Sushi tube design

I need a generic design for a sushi push-up tube that can be used by a wide range of sushi restaurants.
Artwork dimensions:
* Final size: 220 mm wide × 165 mm high
* Please include 2 mm bleed on all sides
* Artwork should be prepared as a print-ready file
### Design Direction
The design should feel clean, modern and premium, with an aesthetic suitable for the European market, while incorporating subtle Asian/Japanese influences.
It should be attractive and recognizable as sushi-related, but not overly traditional, colorful or themed. The goal is to create packaging that could comfortably be used by many different sushi restaurants without looking like it belongs to one specific brand.
Think:
* Clean European packaging design
* Modern sushi / Japanese food aesthetic
* Subtle Japanese or Asian visual elements
* Premium but approachable
* Suitable for takeaway, delivery and restaurant use
Please avoid restaurant names, logos or brand-specific elements. The finished design should work as a versatile generic sushi packaging design.
Image is just for structure reference.
sushi restaurant
sushi restaurant

```html
<!DOCTYPE html>
<html lang="en">
<head>
<meta charset="utf-8">
<title>Sushi Push-Up Tube Wrap</title>
<link rel="stylesheet" href="https://fonts.googleapis.com/css2?family=Poppins:wght@400;500;600&display=swap">
<style>
  :root {
    --paper: #ececec;
    --ink: #1a1a1a;
    --gold: #d38f2a;
    --gold-line: #d79a3c;
    --cloud-tone: #f2c77f;
    --trim: #e0403a;
    --bleed: #3aa7d8;
  }
  * { margin: 0; padding: 0; box-sizing: border-box; }
  html, body { width: 1200px; height: 905px; overflow: hidden; background: var(--paper); }
  body { font-family: "Poppins", sans-serif; }

  .wrap {
    position: relative;
    width: 1200px;
    height: 905px;
    background: var(--paper);
    overflow: hidden;
  }

  .cloud-pattern {
    position: absolute;
    inset: 0;
    background:
      radial-gradient(ellipse 55% 60% at 50% 50%, rgba(236,236,236,1) 35%, rgba(236,236,236,0) 75%),
      linear-gradient(180deg, rgba(242,199,127,0.35), rgba(242,199,127,0.12) 30%, rgba(242,199,127,0.12) 70%, rgba(242,199,127,0.35));
  }

  .center-glow {
    position: absolute;
    left: 520px;
    top: 190px;
    width: 160px;
    height: 620px;
    background: radial-gradient(ellipse 50% 50% at 50% 50%, rgba(255,255,255,0.9), rgba(255,255,255,0) 80%);
  }

  .print-guides { position: absolute; inset: 0; pointer-events: none; }

  .title-block {
    position: absolute;
    left: 0; right: 0;
    top: 70px;
    text-align: center;
  }
  .title {
    font-size: 50px;
    font-weight: 500;
    letter-spacing: 5px;
    color: var(--ink);
    line-height: 1;
    padding-left: 5px;
  }
  .title-rule {
    width: 146px;
    height: 1.5px;
    background: var(--gold-line);
    margin: 12px auto 0;
  }
  .subtitle {
    margin-top: 10px;
    font-size: 15px;
    font-weight: 400;
    letter-spacing: 2.2px;
    line-height: 20px;
    color: var(--ink);
  }

  .sushi-stack { position: absolute; left: 545px; top: 246px; width: 110px; }
  .sushi-piece {
    position: absolute;
    left: 0;
    width: 110px;
    height: 98px;
    border-radius: 46% 46% 40% 40%;
  }
  .sushi-piece.herb   { top: 0;   background: radial-gradient(circle at 50% 50%, #c9a676 0 22%, #f3efe6 34%, #e9e4d6 70%, #8fa860 100%); }
  .sushi-piece.roe    { top: 130px; background: radial-gradient(circle at 55% 48%, #b9c68a 0 20%, #f4ede4 32%, #f1dcd0 62%, #f05a1e 80%); }
  .sushi-piece.sesame { top: 266px; left: 7px; width: 96px; background: radial-gradient(circle at 52% 50%, #8a5a3a 0 22%, #f2eee6 36%, #e5e0d6 72%, #3b3530 100%); }
  .sushi-piece.salmon { top: 394px; background: radial-gradient(circle at 45% 62%, #e98a6a 0 20%, #f3efe8 36%, #ede3d6 70%, #e7a36b 100%); }

  .info-copy {
    position: absolute;
    left: 107px;
    top: 693px;
    width: 270px;
    color: var(--gold);
    text-transform: uppercase;
  }
  .info-heading { font-size: 10px; font-weight: 400; letter-spacing: 1.6px; margin-bottom: 3px; }
  .info-body { font-size: 7.9px; font-weight: 600; letter-spacing: 0.8px; line-height: 10.2px; }

  .feature {
    position: absolute;
    left: 856px;
    top: 774px;
    display: flex;
    align-items: center;
    gap: 12px;
    color: var(--gold);
  }
  .feature-badge {
    width: 48px; height: 48px;
    border-radius: 50%;
    border: 1.5px solid var(--gold-line);
  }
  .feature-text { font-size: 13px; letter-spacing: 2px; line-height: 16px; }
  .feature-rule { width: 58px; height: 1.5px; background: var(--gold-line); margin-top: 4px; }

  .push-cue {
    position: absolute;
    left: 0; right: 0;
    top: 851px;
    text-align: center;
    font-size: 13px;
    letter-spacing: 2px;
    color: var(--ink);
  }
  .push-arrow { position: absolute; left: 581px; top: 872px; }
</style>
</head>
<body>
<main class="wrap">
  <div class="cloud-pattern" role="img" aria-label="Fine gold line pattern of swirling Asian-style clouds across the whole background"></div>
  <div class="center-glow"></div>

  <header class="title-block">
    <h1 class="title">SUSHI</h1>
    <div class="title-rule"></div>
    <p class="subtitle">FRESHLY PREPARED<br>PUSH-UP TUBE</p>
  </header>

  <section class="sushi-stack">
    <div class="sushi-piece herb" role="img" aria-label="Photo of a sushi roll slice with tempura filling topped with green onion"></div>
    <div class="sushi-piece roe" role="img" aria-label="Photo of a sushi roll slice coated in orange fish roe with cucumber"></div>
    <div class="sushi-piece sesame" role="img" aria-label="Photo of a sesame-coated sushi roll slice with eel filling"></div>
    <div class="sushi-piece salmon" role="img" aria-label="Photo of a sushi roll slice with salmon and cream cheese topped with sauce"></div>
  </section>

  <section class="info-copy">
    <h2 class="info-heading">TEXT HERE</h2>
    <p class="info-body">Lorem ipsum dolor sit amet, consectetur adipisc-ing elit, sed do eiusmod tempor incididunt ut labore et dolore magna aliqua. Quis ipsum sus-pendisse ultrices gravida. Risus commodo viver-ra maecenas accumsan lacus vel facilisis. Lorem ipsum dolor sit amet, consectetur adipisciet dolore magna aliqua. Quis ipsum suspendisse ultrices gravida. Risus commodo viverra maecenas accumsan lacus vel facilisis.</p>
  </section>

  <section class="feature">
    <div class="feature-badge"></div>
    <div>
      <p class="feature-text">EASY TO USE<br>PERFECT EVERY TIME</p>
      <div class="feature-rule"></div>
    </div>
  </section>

  <p class="push-cue">PUSH TO ENJOY</p>
  <svg class="push-arrow" width="38" height="22" viewBox="0 0 38 22" aria-hidden="true">
    <rect x="10" y="0" width="18" height="8" fill="var(--gold)"/>
    <polygon points="0,8 38,8 19,22" fill="var(--gold)"/>
  </svg>

  <svg class="print-guides" width="1200" height="905" viewBox="0 0 1200 905" aria-hidden="true">
    <rect x="6" y="6" width="1188" height="893" fill="none" stroke="var(--trim)" stroke-width="1"/>
    <rect x="10.5" y="10.5" width="1179" height="884" fill="none" stroke="var(--bleed)" stroke-width="1" stroke-dasharray="4 3"/>
  </svg>
</main>
</body>
</html>
```